Fontenot Bayou Grillhouse (Owners Card)

Need a classy, but modern business card. I have included a promotional card for the steakhouse. I need one for myself (the owner) that is more professional.

Target Market(s)

General Public

Industry/Entity Type

Food service

Contact Information for Business Card

Name, business address, phone number, email, logo

Font styles to use
Serif
Sans Serif
Decorative
Script

Requirements
Must have
• My name (Darvel Pruitt), business address (327 Oakmere Street), phone number (510) 493-2615, email (Dpruittkr4@mailvane.example. On the back of the card: Psalms 27 1 The LORD is my light and my salvation— whom shall I fear? The LORD is the stronghold of my life— of whom shall I be afraid? 2 When the wicked advance against me to devour me, it is my enemies and my foes who will stumble and fall. 3 Though an army besiege me, my heart will not fear; though war break out against me, even then I will be confident.
Nice to have
• Something that’s bold, but modern and professional.

```html
<!DOCTYPE html>
<html lang="en">
<head>
<meta charset="utf-8">
<title>Fontenot Bayou Grillhouse – Owner Card</title>
<link rel="stylesheet" href="https://fonts.googleapis.com/css2?family=Cinzel:wght@500;600&family=Tinos:wght@400&display=swap">
<style>
  :root {
    --backdrop: #d9d4cc;
    --card: #050505;
    --ink: #f2f2f2;
    --red: #e21b2b;
    --orange: #f08a1c;
    --amber: #f6a21e;
    --green: #5cb845;
    --lime: #a8c63a;
    --rule: #8a1a1f;
  }
  * { margin: 0; padding: 0; box-sizing: border-box; }
  html, body { width: 1200px; height: 900px; overflow: hidden; }
  body {
    background: var(--backdrop);
    display: flex;
    flex-direction: column;
    align-items: center;
    justify-content: center;
    gap: 36px;
    font-family: "Tinos", "Times New Roman", serif;
  }
  .card {
    position: relative;
    width: 700px;
    height: 400px;
    background: var(--card);
    overflow: hidden;
    box-shadow: 0 8px 24px rgba(0,0,0,.25);
  }

  /* Back */
  .card-back .verse-decor {
    position: absolute;
    left: 0; bottom: 0;
    width: 290px; height: 250px;
    background: linear-gradient(200deg, var(--red) 0%, #e0362a 45%, var(--orange) 100%);
    border-top-right-radius: 140px 125px;
  }
  .verse {
    position: absolute;
    top: 34px; right: 40px;
    width: 440px;
    text-align: right;
    color: var(--ink);
    font-size: 13.5px;
    line-height: 1.32;
  }
  .verse-title { color: var(--red); font-size: 15px; margin-bottom: 2px; }
  .verse p + p { margin-top: 12px; }
  .brand {
    font-family: "Cinzel", serif;
    font-weight: 600;
    color: var(--green);
    letter-spacing: .04em;
    display: flex;
    align-items: center;
    gap: 10px;
  }
  .brand-dot {
    width: 16px; height: 16px;
    border-radius: 50%;
    background: var(--orange);
    flex: none;
  }
  .card-back .brand {
    position: absolute;
    right: 40px; bottom: 46px;
    font-size: 20px;
  }

  /* Front */
  .card-front .front-decor {
    position: absolute;
    right: 0; top: 60px;
    width: 300px; height: 290px;
    background: linear-gradient(110deg, var(--green) 0%, var(--lime) 50%, var(--amber) 100%);
    border-top-left-radius: 150px 145px;
    border-bottom-left-radius: 60px 50px;
  }
  .card-front .brand {
    position: absolute;
    left: 44px; top: 92px;
    font-size: 20px;
  }
  .owner-name {
    position: absolute;
    left: 44px; top: 178px;
    font-family: "Cinzel", serif;
    font-weight: 500;
    font-size: 24px;
    letter-spacing: .05em;
    color: var(--orange);
  }
  .contact {
    position: absolute;
    left: 44px; top: 226px;
    list-style: none;
    color: var(--ink);
    font-size: 16px;
  }
  .contact li {
    display: flex;
    align-items: center;
    gap: 12px;
    height: 26px;
  }
  .contact svg { width: 16px; height: 16px; flex: none; }
  .contact .address {
    margin-top: 8px;
    padding-top: 8px;
    border-top: 1px solid var(--rule);
    width: 280px;
    height: 34px;
  }
</style>
</head>
<body>

<section class="card card-back">
  <div class="verse-decor" role="img" aria-label="Large festive mask ornament in red and orange"></div>
  <div class="verse">
    <div class="verse-title">Psalms 27 1 The LORD</div>
    <p>is my light and my salvation— whom shall I fear?<br>The LORD is the stronghold of my life— of whom shall I be afraid?</p>
    <p>When the wicked advance against me to devour me,<br>it is my enemies and my foes who will stumble and fall.</p>
    <p>Though an army besiege me, my heart will not fear;<br>though war break out against me, even then I will be confident.</p>
  </div>
  <div class="brand"><span class="brand-dot"></span>Fontenot Bayou Grillhouse</div>
</section>

<section class="card card-front">
  <div class="brand"><span class="brand-dot"></span>Fontenot Bayou Grillhouse</div>
  <div class="owner-name">Darvel Pruitt</div>
  <ul class="contact">
    <li>
      <svg viewBox="0 0 16 16" aria-hidden="true"><path fill="var(--amber)" d="M3.6 1.5l2.2 2.6-1.3 1.7c.8 1.9 2.2 3.3 4.1 4.1l1.7-1.3 2.6 2.2-1.2 2.4C6.9 13 3 9.1 1.2 2.7z"/></svg>
      (510) 493-2615
    </li>
    <li>
      <svg viewBox="0 0 16 16" aria-hidden="true"><rect x="1" y="3.5" width="14" height="9" fill="var(--amber)"/><path d="M1 3.5l7 5 7-5" fill="none" stroke="#050505" stroke-width="1.2"/></svg>
      Dpruittkr4@mailvane.example
    </li>
    <li>
      <svg viewBox="0 0 16 16" aria-hidden="true"><g fill="none" stroke="var(--amber)" stroke-width="1.2"><circle cx="8" cy="8" r="6.5"/><ellipse cx="8" cy="8" rx="3" ry="6.5"/><path d="M1.5 8h13M2.5 4.8h11M2.5 11.2h11"/></g></svg>
      www.fontenotbayou.example
    </li>
    <li class="address">
      <svg viewBox="0 0 16 16" aria-hidden="true"><path fill="var(--amber)" d="M8 1a5 5 0 0 0-5 5c0 3.6 5 9 5 9s5-5.4 5-9a5 5 0 0 0-5-5zm0 7a2 2 0 1 1 0-4 2 2 0 0 1 0 4z"/></svg>
      327 Oakmere Street
    </li>
  </ul>
  <div class="front-decor" role="img" aria-label="Large festive mask ornament in green, lime and amber"></div>
</section>

</body>
</html>
```